SilverLedgerOak - Double Sided Business Card

We are looking for design options or our business cards. We are a Business Solutions and HR solutions Provider - the theme is business, for this card.

Our brand colours are represented within our logo.

Details needed to be put on the front of the business card are:

Employees name: [Sample Name]
Role: [Sample Role]

Address: Suite 4 - Level 3/48 Halloran Avenue Parramatta NSW 2150
M: 0000 000 000
P: 1300 847 213
F: 1300 847 286
E: sample@silverledgeroak.com.au
www.silverledgeroak.com.au
Updates

Reason: Hello, could we please increase our deadline by 5 days. Thanking you, Tess

Target Market(s)

Business Owners, also Candidates looking for Employment

Industry/Entity Type

Business

Contact Information for Business Card

Role: [Sample Role]

M: 0000 000 000
P: 1300 847 213
F: 1300 847 286

Font styles to use
Sans Serif

Colors
3276b5
3176b5
0455a3
85abd2
cfdeed
ffffff
000000
1b1b1b
757575

Requirements
Must have
• Details needed to be put on the front of the business card are:
• Employees name: [Sample Name]
• Role: [Sample Role]
• Address: Suite 4 - Level 3/48 Halloran Avenue Parramatta NSW 2150
• M: 0000 000 000
• P: 1300 847 213
• F: 1300 847 286
• E: sample@silverledgeroak.com.au
• www.silverledgeroak.com.au
Nice to have
• Simplicity, clean and professional.

```html
<!DOCTYPE html>
<html lang="en">
<head>
<meta charset="utf-8">
<title>SilverLedgerOak Business Card</title>
<link rel="stylesheet" href="https://fonts.googleapis.com/css2?family=Montserrat:wght@400;500;600;700&display=swap">
<style>
  :root {
    --navy: #0d2a4a;
    --blue: #0455a3;
    --blue-mid: #3276b5;
    --blue-soft: #85abd2;
    --white: #ffffff;
    --ink: #1b1b1b;
    --grey: #757575;
    --stage: #e9edf2;
  }
  * { margin: 0; padding: 0; box-sizing: border-box; }
  html, body { width: 1200px; height: 864px; overflow: hidden; }
  body {
    background: var(--stage);
    font-family: "Montserrat", Arial, sans-serif;
    display: flex;
    align-items: center;
    justify-content: center;
    gap: 28px;
  }
  .card {
    width: 556px;
    height: 318px;
    position: relative;
    box-shadow: 0 6px 18px rgba(13, 42, 74, 0.18);
  }
  /* Back side */
  .card-back {
    background: var(--navy);
    color: var(--white);
    display: flex;
    flex-direction: column;
    align-items: center;
    justify-content: center;
  }
  .brand {
    display: flex;
    align-items: center;
    gap: 12px;
  }
  .brand-square {
    width: 30px; height: 30px;
    background: var(--blue-mid);
  }
  .brand-name {
    font-weight: 700;
    font-size: 30px;
    letter-spacing: 0.5px;
    white-space: nowrap;
  }
  .card-back .brand-name { color: var(--white); }
  .tagline {
    margin-top: 10px;
    font-size: 10px;
    font-weight: 600;
    color: var(--white);
    border-top: 1px solid var(--blue-soft);
    padding-top: 6px;
    white-space: nowrap;
  }
  .back-web {
    margin-top: 30px;
    font-size: 14px;
    letter-spacing: 0.3px;
  }
  /* Front side */
  .card-front { background: var(--white); }
  .card-front .brand {
    position: absolute;
    top: 38px; right: 36px;
  }
  .card-front .brand-square { width: 22px; height: 22px; background: var(--blue); }
  .card-front .brand-name { font-size: 21px; color: var(--navy); }
  .card-front .tagline {
    position: absolute;
    top: 74px; right: 36px;
    margin-top: 0;
    color: var(--ink);
    font-size: 7.5px;
    border-top-color: var(--blue-mid);
    padding-top: 4px;
  }
  .person-name {
    position: absolute;
    left: 36px; top: 150px;
    font-size: 21px; font-weight: 600; color: var(--ink);
    line-height: 26px;
  }
  .divider {
    position: absolute;
    left: 36px; right: 36px; top: 182px;
    height: 1px;
    background: var(--blue);
  }
  .person-role {
    position: absolute;
    left: 36px; top: 188px;
    font-size: 14px; color: var(--grey);
    line-height: 18px;
  }
  .contacts {
    position: absolute;
    left: 36px; bottom: 28px;
    list-style: none;
  }
  .contacts li {
    display: flex;
    align-items: center;
    gap: 8px;
    font-size: 14px;
    color: var(--ink);
    line-height: 21px;
  }
  .contacts svg { width: 13px; height: 13px; fill: var(--blue); flex: none; }
  .address {
    position: absolute;
    right: 36px; bottom: 70px;
    text-align: right;
    font-size: 13px;
    line-height: 19px;
    color: var(--grey);
  }
  .address .web { color: var(--ink); font-size: 14px; }
</style>
</head>
<body>
  <section class="card card-back" aria-label="Card back">
    <div class="brand">
      <span class="brand-square"></span>
      <span class="brand-name">SilverLedgerOak</span>
    </div>
    <p class="tagline">Guiding growing firms toward steady and lasting success</p>
    <p class="back-web">www.silverledgeroak.com.au</p>
  </section>

  <section class="card card-front" aria-label="Card front">
    <div class="brand">
      <span class="brand-square"></span>
      <span class="brand-name">SilverLedgerOak</span>
    </div>
    <p class="tagline">Guiding growing firms toward steady and lasting success</p>

    <p class="person-name">Sam Carter</p>
    <div class="divider"></div>
    <p class="person-role">President</p>

    <ul class="contacts">
      <li>
        <svg viewBox="0 0 16 16" aria-hidden="true"><path d="M3.6 1.2l2.3 2.6-1.4 1.9c.9 2 2.6 3.7 4.6 4.6l1.9-1.4 2.6 2.3-1.4 2.6C7 13.6 2.4 9 1 3.8z"/></svg>
        012-555-0142
      </li>
      <li>
        <svg viewBox="0 0 16 16" aria-hidden="true"><path d="M4 1h8v14H4zM5.5 2.5v9h5v-9zM7.2 12.4h1.6v1.4H7.2z" fill-rule="evenodd"/></svg>
        012-555-0187
      </li>
      <li>
        <svg viewBox="0 0 16 16" aria-hidden="true"><path d="M4 1h8v4H4zM1 6h14v6h-3v3H4v-3H1zM5.5 10v3.5h5V10z" fill-rule="evenodd"/></svg>
        012-555-0187
      </li>
      <li>
        <svg viewBox="0 0 16 16" aria-hidden="true"><path d="M1 3h14v10H1zM2.5 4.5L8 9l5.5-4.5v7h-11z" fill-rule="evenodd"/></svg>
        info@silverledgeroak.com.au
      </li>
    </ul>

    <div class="address">
      <p>Street Name Ave, Suite 100</p>
      <p>State, Zip Code, Country</p>
      <p class="web">www.silverledgeroak.com.au</p>
    </div>
  </section>
</body>
</html>
```